Realtor resource

This is a website that provides resources for Realtors and their customers (home buyers and sellers).

There are 5 pages that I need redesigned:

1. Homepage: https://brightporchhelp.com/
2. Support Page/Contact Us: https://brightporchhelp.com/contact-us/
3. Agent Dashboard - See attached screenshot
4. Real Estate Documents page - See attached screenshot
5. Real Estate Contract page - see attached screenshot

Target Market(s)

Real estate agents and their customers.

Industry/Entity Type

Real Estate

Number of Pages Required

5+ page

Requirements
Must have
• Please use a modern design and incorporate design with current logo.

```html
<!DOCTYPE html>
<html lang="en">
<head>
<meta charset="utf-8">
<title>BrightPorch – Real Estate Contracts Explained</title>
<link rel="stylesheet" href="https://fonts.googleapis.com/css2?family=Montserrat:wght@400;500;600;700&display=swap">
<style>
  :root {
    --orange: #fb9300;
    --orange-soft: #f7a500;
    --orange-pale: #fdc98a;
    --ink: #111111;
    --ink-soft: #3a2a1a;
    --band: #f6f5f5;
    --footer: #252525;
    --rule: #b5b5b5;
    --white: #ffffff;
  }
  * { box-sizing: border-box; margin: 0; padding: 0; }
  html, body { width: 1200px; height: 2400px; overflow: hidden; }
  body { position: relative; background: var(--white); font-family: "Montserrat", sans-serif; color: var(--ink); }
  .abs { position: absolute; }

  .topbar { left: 0; top: 0; width: 1200px; height: 68px; background: var(--band); }
  .brand { left: 244px; top: 22px; font-size: 17px; font-weight: 600; display: flex; align-items: center; gap: 5px; }
  .brand-dot { width: 16px; height: 16px; border-radius: 50%; background: var(--orange-soft); }
  .user-icon { left: 820px; top: 23px; }
  .login { left: 854px; top: 24px; width: 111px; height: 21px; border-radius: 11px; background: var(--orange-soft); font-size: 13px; font-weight: 500; text-align: center; line-height: 21px; }

  .nav { top: 98px; font-size: 14px; font-weight: 600; }
  .nav-home { left: 386px; color: var(--orange); }
  .nav-support { left: 453px; }
  .nav-docs { left: 536px; }
  .search-field { left: 730px; top: 98px; width: 142px; height: 18px; border: 1.5px solid var(--ink); border-radius: 5px; font-family: Georgia, serif; font-size: 11px; color: #777; padding-left: 7px; line-height: 15px; }
  .search-icon { left: 896px; top: 100px; }

  .hero { left: 166px; top: 144px; width: 888px; height: 500px; background: linear-gradient(135deg, #f3a13a, #f8b14a 45%, #e89a2c); border: 1px solid #f5a640; }
  .hero-panel { left: 220px; top: 215px; width: 298px; height: 364px; background: #b0702a; }
  .hero-keys { left: 232px; top: 250px; width: 223px; height: 294px; background: linear-gradient(90deg, #8dbf6a, #d9cfa8 50%, #6b4a2a); }
  .hero-card { left: 518px; top: 179px; width: 272px; height: 420px; background: var(--white); }
  .hero-desk { left: 541px; top: 201px; width: 227px; height: 171px; background: linear-gradient(135deg, #3b3b3b, #d7d2cb 60%, #f0f0f0); }
  .hero-title-box { left: 570px; top: 316px; width: 472px; height: 265px; background: linear-gradient(160deg, #6b7480, #4d5a4a 55%, #3d4a5a); border: 2px solid #8c8c8c; }
  .hero-title { left: 597px; top: 327px; width: 440px; color: var(--white); font-size: 38px; font-weight: 700; line-height: 49px; letter-spacing: 0.5px; text-shadow: 0 1px 3px rgba(0,0,0,.5); }

  .band { left: 0; top: 678px; width: 1200px; height: 466px; background: var(--band); }
  .realtor-photo { left: 286px; top: 704px; width: 641px; height: 426px; background: linear-gradient(135deg, #c98a45, #e7b071 45%, #a9661f); }
  .promo-text { background: rgba(255, 204, 140, .85); font-size: 24px; font-weight: 500; line-height: 37px; }
  .realtor-text { left: 324px; top: 899px; width: 565px; height: 141px; padding: 17px 12px; }
  .cta { background: var(--orange); border: 3px solid #e98800; border-radius: 22px; text-align: center; font-size: 38px; font-weight: 500; color: #2a1a05; box-shadow: 0 2px 4px rgba(0,0,0,.2); }
  .realtor-cta { left: 428px; top: 1040px; width: 357px; height: 88px; line-height: 82px; letter-spacing: 1.5px; }

  .clients-frame { left: 288px; top: 1180px; width: 639px; height: 434px; background: var(--orange-pale); }
  .clients-photo { left: 311px; top: 1198px; width: 591px; height: 399px; background: linear-gradient(120deg, #f4a868, #f7c38e 50%, #e79a55); }
  .clients-text { left: 355px; top: 1384px; width: 534px; height: 140px; padding: 18px 0 0 68px; background: rgba(255, 214, 160, .6); color: var(--ink-soft); }
  .clients-cta { left: 436px; top: 1524px; width: 356px; height: 89px; line-height: 82px; color: #3a2206; }

  .rule { left: 333px; top: 1657px; width: 542px; height: 1px; background: var(--rule); }
  .help { left: 0; top: 1745px; width: 1200px; text-align: center; font-size: 25px; font-weight: 500; }
  .contact-tag { left: 522px; top: 1785px; width: 159px; height: 31px; background: var(--orange); font-size: 25px; font-weight: 700; text-align: center; line-height: 31px; }

  .label { left: 349px; font-size: 16px; font-weight: 600; }
  .field { border: 1.5px solid var(--orange-soft); border-radius: 17px; font-size: 12px; color: #777; padding-left: 22px; line-height: 32px; }
  .first-name { left: 331px; top: 1890px; width: 232px; height: 34px; }
  .last-name { left: 643px; top: 1890px; width: 233px; height: 34px; }
  .email { left: 331px; top: 1971px; width: 312px; height: 34px; }
  .message { left: 331px; top: 2042px; width: 312px; height: 176px; border-radius: 18px; }
  .submit { left: 331px; top: 2232px; width: 127px; height: 34px; border-radius: 17px; background: var(--orange); font-size: 16px; font-weight: 700; text-align: center; line-height: 34px; }

  .footer { left: 0; top: 2331px; width: 1200px; height: 69px; background: var(--footer); color: var(--white); text-align: center; font-size: 18px; font-weight: 500; line-height: 70px; }
</style>
</head>
<body>
  <header>
    <div class="abs topbar"></div>
    <div class="abs brand">BrightPorch<span class="brand-dot"></span></div>
    <svg class="abs user-icon" width="22" height="24" viewBox="0 0 22 24" aria-hidden="true">
      <circle cx="11" cy="6.5" r="5.5" fill="#111"/>
      <path d="M1 23 Q1 13 11 13 Q21 13 21 23 Z" fill="#111"/>
    </svg>
    <div class="abs login">Login</div>
    <nav>
      <span class="abs nav nav-home">Home</span>
      <span class="abs nav nav-support">Support</span>
      <span class="abs nav nav-docs">Real Estat Documents</span>
    </nav>
    <div class="abs search-field">search</div>
    <svg class="abs search-icon" width="14" height="14" viewBox="0 0 14 14" aria-hidden="true">
      <circle cx="6" cy="6" r="4.5" fill="none" stroke="#111" stroke-width="1.3"/>
      <line x1="9.3" y1="9.3" x2="13" y2="13" stroke="#111" stroke-width="1.3"/>
    </svg>
  </header>

  <main>
    <section>
      <div class="abs hero" role="img" aria-label="Aerial view of a suburban neighbourhood tinted orange"></div>
      <div class="abs hero-panel"></div>
      <div class="abs hero-keys" role="img" aria-label="House keys hanging in a front door lock"></div>
      <div class="abs hero-card"></div>
      <div class="abs hero-desk" role="img" aria-label="Agent pointing at a laptop while reviewing a contract"></div>
      <div class="abs hero-title-box" role="img" aria-label="Aerial view of homes and streets"></div>
      <h1 class="abs hero-title">Real Estate Contracts Explained<br>in plain language<br>by Texas real estate attorneys.</h1>
    </section>

    <section>
      <div class="abs band"></div>
      <div class="abs realtor-photo" role="img" aria-label="Hands signing a real estate agreement at a table"></div>
      <p class="abs promo-text realtor-text">We&nbsp; provide real estate agents with valuable industry insights, strategies, and tips to grow their business.</p>
      <div class="abs cta realtor-cta">REALTOR</div>
    </section>

    <section>
      <div class="abs clients-frame"></div>
      <div class="abs clients-photo" role="img" aria-label="New homeowners receiving house keys"></div>
      <p class="abs promo-text clients-text">We are dedicated<br>to offering our clients superior<br>Customer Service.</p>
      <div class="abs cta clients-cta">Buyers &amp; Sellers</div>
    </section>

    <div class="abs rule"></div>

    <section>
      <h2 class="abs help" style="font-weight:500">Need Help?</h2>
      <div class="abs contact-tag">Contact US</div>
      <form>
        <span class="abs label" style="top:1862px">Name *</span>
        <div class="abs field first-name">First Name</div>
        <div class="abs field last-name">Last Name</div>
        <span class="abs label" style="top:1945px">Email *</span>
        <div class="abs field email"></div>
        <span class="abs label" style="top:2016px">Comment or Message *</span>
        <div class="abs field message"></div>
        <div class="abs submit">Submit</div>
      </form>
    </section>
  </main>

  <footer class="abs footer">© Copyright 2019. All Rights Reserved.</footer>
</body>
</html>
```